Clothing Brand E-Commerce Website Design

We would like you to provide an ecommerce design template in layered PSD for our clothing/fashion brand website called "TrelWick".
We want the site to have a simple but sleek design similar to the following sites:
http://www.pivorane.com/
http://corvatelle.com/
http://www.dulvenor.com/
We want it to look stunning and blow the example sites out of the water. For color scheme, please use your imagination and try to impress us with your creativity.
We like teal and beige pink, with teal dominant.
Teal #7AFFFF / #46C6C6
Beige/pink #FF7B7C / #C74646
We want you to develop the design for 3 pages:
1) Home Page
Samples:
http://www.pivorane.com/
http://corvatelle.com/
http://www.dulvenor.com/
2) Products List Page (e.g., lists all "Dresses" when category is selected)
http://www.pivorane.com/shop/casual-dresses
http://www.dulvenor.com/index.php?main_page=index&cPath=3
http://corvatelle.com/modest-dresses.html
http://www.quillmarsh.com/Product/Category.aspx?br=q47&category=dress_maxi
3) Product Detail Page (e.g., individual product page with "Add to Cart")
http://www.pivorane.com/shop/dresses/lumen-fern-dress
http://corvatelle.com/modest-dresses/modest-dress-tova.html
http://www.dulvenor.com/index.php?main_page=product_info&cPath=3&products_id=297
Industry/Entity Type
Fashion

```html
<!DOCTYPE html>
<html lang="en">
<head>
<meta charset="utf-8">
<title>TrelWick – Home</title>
<link rel="stylesheet" href="https://fonts.googleapis.com/css2?family=Open+Sans:wght@400;600&family=Roboto+Condensed:wght@400&display=swap">
<style>
:root{
  --pink:#f47b7c;
  --pink-soft:rgba(244,123,124,.78);
  --teal:#46c6c6;
  --text:#444;
  --muted:#777;
  --line:#d8d8d8;
  --bar:#f1f1f1;
  --white:#fff;
}
*{box-sizing:border-box;margin:0;padding:0}
html,body{width:860px;height:1200px;overflow:hidden}
body{position:relative;background:var(--white);font-family:"Open Sans",Arial,sans-serif;color:var(--text)}
.abs{position:absolute}

.top-bar{left:0;top:0;width:860px;height:30px;background:var(--bar);border-bottom:2px dotted #ddd;font-size:9.5px;color:var(--muted)}
.top-bar .call{left:79px;top:9px}
.top-bar .account{left:571px;top:9px}
.top-bar .cart{left:693px;top:9px}

.brand{left:78px;top:50px;font-size:26px;font-weight:600;letter-spacing:1px;color:var(--pink)}
.search{left:572px;top:55px;width:209px;height:22px;border:1px solid #ccc;background:#fafafa;font-size:9.5px;color:#888;padding:4px 8px}
.search svg{position:absolute;right:8px;top:5px}

.main-nav{left:0;top:100px;width:860px;height:34px;border-top:1px dashed var(--line);border-bottom:1px dashed var(--line);display:flex;justify-content:center;align-items:center;font-size:10.5px;color:#333}
.main-nav span{padding:0 18px}
.main-nav .sep{padding:0}
.main-nav .current{color:var(--teal)}

.hero{left:0;top:143px;width:860px;height:305px;border-top:3px solid #bfc3c3;border-bottom:3px solid #bfc3c3;background:linear-gradient(100deg,#e9b27c 0%,#d9996e 30%,#b8876a 55%,#8e8f62 80%,#6f8a55 100%)}
.hero-line{left:79px;background:rgba(255,255,255,.85);color:#333;font-size:19px;padding:1px 4px;letter-spacing:.3px}
.hero-line.one{top:246px}
.hero-line.two{top:283px}
.hero-line b{color:var(--pink);font-weight:600}

.tile{top:465px;width:226px;height:118px;overflow:hidden}
.tile .cap{position:absolute;left:0;bottom:0;width:100%;height:27px;background:var(--pink-soft);color:#fff;font-size:12.5px;font-weight:600;padding:5px 11px;letter-spacing:.2px}
.tile-a{left:79px;background:linear-gradient(135deg,#3a7fa0,#d96a7c 60%,#2d2b30)}
.tile-b{left:318px;background:linear-gradient(160deg,#8a5a32,#d7a65a 50%,#f0c070)}
.tile-c{left:556px;background:linear-gradient(120deg,#c9a98a,#e6d6c4 50%,#b08d6e)}

.panel{top:625px;width:341px;height:284px;border:1px solid var(--line)}
.panel-title{top:616px;background:var(--white);color:var(--pink);font-size:13px;padding:0 10px}
.panel-title::before,.panel-title::after{content:"";position:absolute;top:8px;width:4px;height:4px;border-radius:50%;background:#ccc}
.panel-title::before{left:-8px}
.panel-title::after{right:-8px}
.product{width:100px;text-align:center}
.product .shot{width:80px;height:184px;margin:0 auto;background:linear-gradient(180deg,#f1e6dc,#d9c4b4)}
.product .name{margin-top:12px;font-size:12.5px;color:#888}
.product .price{font-size:12.5px;color:#777;margin-top:1px}
.product .btn{display:inline-block;margin-top:4px;border:2px solid var(--teal);background:var(--teal);color:#fff;font-size:9.5px;padding:3px 5px;box-shadow:inset 0 0 0 1px #fff}
.arrow{width:17px;height:17px;border-radius:50%;background:#e6e6e6}

.footer{left:0;top:950px;width:860px;height:213px;background:#f0f0f0;border-top:2px dotted #ddd}
.f-head{font-family:"Roboto Condensed",Arial,sans-serif;font-size:14px;color:#222;top:974px}
.f-rule{top:999px;width:32px;height:3px;background:var(--pink)}
.f-list{top:1027px;font-size:8.3px;color:#555;line-height:17.2px}
.field{left:428px;width:158px;background:var(--white);border:1px solid #ddd;font-size:8.5px;color:#555;padding:4px 10px}
.submit{left:531px;top:1124px;width:54px;height:19px;background:var(--pink);color:#fff;font-size:9px;text-align:center;padding-top:3px}
.pay{top:1013px;height:20px;width:34px;background:var(--white);border:1px solid #ddd;font-size:6.5px;text-align:center;padding-top:5px;color:#335}
.f-text{font-size:8.3px;color:#555;line-height:12px}

.bottom-bar{left:0;top:1163px;width:860px;height:37px;border-top:1px solid #ddd;background:var(--white)}
.copy{left:78px;top:1177px;font-size:7.2px;font-weight:600;color:#222}
.social{top:1175px;font-size:8px;font-weight:600;color:#222}
</style>
</head>
<body>

<div class="abs top-bar">
  <span class="abs call">Call Us Now: 555 014 23307</span>
  <span class="abs account">Sign In &nbsp;| &nbsp;Register</span>
  <span class="abs cart">Shopping Cart $0.00</span>
</div>

<div class="abs brand">TRELWICK</div>
<div class="abs search">Search...
  <svg width="10" height="10" viewBox="0 0 10 10"><circle cx="4" cy="4" r="3" fill="none" stroke="#888" stroke-width="1.2"/><line x1="6.3" y1="6.3" x2="9" y2="9" stroke="#888" stroke-width="1.2"/></svg>
</div>

<nav class="abs main-nav">
  <span class="current">HOME</span><span class="sep">|</span>
  <span>ABOUT US</span><span class="sep">|</span>
  <span>PRODUCTS</span><span class="sep">|</span>
  <span>NEW ARRIVALS</span><span class="sep">|</span>
  <span>CLOTHING</span><span class="sep">|</span>
  <span>VINTAGE</span><span class="sep">|</span>
  <span>SALE</span><span class="sep">|</span>
  <span>CONTACT US</span>
</nav>

<div class="abs hero" role="img" aria-label="Sunlit photo of a young woman in a knit beanie and sunglasses leaning on a railing by a garden path"></div>
<div class="abs hero-line one">WELCOME TO <b>TRELWICK</b></div>
<div class="abs hero-line two">SPRING SUMMER 2014</div>

<div class="abs tile tile-a" role="img" aria-label="Photo of a group of friends in sunglasses and bright summer clothes"><div class="cap">NEW COLLECTION 2014</div></div>
<div class="abs tile tile-b" role="img" aria-label="Photo of a woman in a wide straw hat and white sunglasses"><div class="cap">VIEW SUMMER COLLECTION</div></div>
<div class="abs tile tile-c" role="img" aria-label="Photo of a woman in a plaid shirt sitting beside a bicycle"><div class="cap">NEW ARRIVALS READY TO WEAR</div></div>

<div class="abs panel" style="left:80px"></div>
<div class="abs panel-title" style="left:174px">FEATURED PRODUCTS</div>
<div class="abs arrow" style="left:93px;top:746px"></div>
<div class="abs arrow" style="left:387px;top:746px"></div>
<div class="abs product" style="left:106px;top:640px"><div class="shot" role="img" aria-label="Product photo of a model wearing a beige coat"></div><div class="name">Lorem Ipsum</div><div class="price">$123.00</div><span class="btn">Add To Cart</span></div>
<div class="abs product" style="left:297px;top:640px"><div class="shot" role="img" aria-label="Product photo of a model wearing a beige coat"></div><div class="name">Lorem Ipsum</div><div class="price">$123.00</div><span class="btn">Add To Cart</span></div>

<div class="abs panel" style="left:439px"></div>
<div class="abs panel-title" style="left:544px">LATEST PRODUCTS</div>
<div class="abs arrow" style="left:452px;top:746px"></div>
<div class="abs arrow" style="left:746px;top:746px"></div>
<div class="abs product" style="left:465px;top:640px"><div class="shot" role="img" aria-label="Product photo of a model wearing a beige coat"></div><div class="name">Lorem Ipsum</div><div class="price">$123.00</div><span class="btn">Add To Cart</span></div>
<div class="abs product" style="left:656px;top:640px"><div class="shot" role="img" aria-label="Product photo of a model wearing a beige coat"></div><div class="name">Lorem Ipsum</div><div class="price">$123.00</div><span class="btn">Add To Cart</span></div>

<footer class="abs footer"></footer>
<div class="abs f-head" style="left:94px">WELCOME</div>
<div class="abs f-rule" style="left:94px"></div>
<div class="abs f-list" style="left:95px">Lorem ipsum dotslor sicts adfmet<br>Nam non disam ersaddos dasssd<br>Vestibulum aliquet eros ut ipsum<br>Nullam blandit tristique lacuss is<br>Ut quis ante dui, eget scelerisque<br>Praesent tincidunt duid id sapien</div>

<div class="abs f-head" style="left:273px">SITE LINKS</div>
<div class="abs f-rule" style="left:273px"></div>
<div class="abs f-list" style="left:273px">Home (we start here)<br>About (get to know us better)<br>Services (all we do)<br>Galleries (see our work)<br>Blog (the news)<br>Contact (get in touch with us)</div>

<div class="abs f-head" style="left:426px">QUICK CONTACT</div>
<div class="abs f-rule" style="left:426px"></div>
<div class="abs field" style="top:1018px;height:20px">Name</div>
<div class="abs field" style="top:1048px;height:20px">Email</div>
<div class="abs field" style="top:1078px;height:32px">Message</div>
<div class="abs submit">Submit</div>

<div class="abs f-head" style="left:612px">PAYMENT OPTIONS</div>
<div class="abs f-rule" style="left:612px"></div>
<div class="abs pay" style="left:612px">Paywell</div>
<div class="abs pay" style="left:653px">Cardora</div>
<div class="abs pay" style="left:694px">Eastbridge</div>
<div class="abs pay" style="left:735px">Vantra</div>
<div class="abs f-text" style="left:613px;top:1045px">Lorem ipsum dolor sit amet, consecteer<br>adipiscing elit.</div>
<div class="abs f-head" style="left:612px;top:1078px">OUR OFFICE</div>
<div class="abs f-rule" style="left:612px;top:1106px"></div>
<div class="abs f-text" style="left:613px;top:1122px">Ferrow Lane 24 - Office Location<br>Haldenby - HB - 401276 - 0061 55501234</div>

<div class="abs bottom-bar"></div>
<div class="abs copy">COPYRIGHT 2014 TRELWICK . ALL RIGHTS RESERVED.</div>
<div class="abs social" style="left:680px">Glint</div>
<div class="abs social" style="left:706px">Chirper</div>
<div class="abs social" style="left:742px">Folio</div>
<div class="abs social" style="left:765px">Linkmere</div>

</body>
</html>
```